Morrow Interiors

Hi, can you please make this design up for me. Morrow interiors text to front and Beatrice Morrow text to back in black. Small love hearts to be black. Mobile number to front text and back mobile number and email address text to be white. Open to your input 🙂 Thanks in advance! Beatrice

Industry/Entity Type

Interior Design

Colors

Designer to choose only greyscale colors for use in the design.

Requirements
Must have
• Little love hearts for dot on i

```html
<!DOCTYPE html>
<html lang="en">
<head>
<meta charset="utf-8">
<title>Morrow Interiors – Business Cards</title>
<link rel="stylesheet" href="https://fonts.googleapis.com/css2?family=Fira+Sans:wght@400;500&display=swap">
<style>
  :root {
    --page: #e4e4e4;
    --card-dark: #2e2e2e;
    --band-light: #ffffff;
    --ink-dark: #333333;
    --ink-light: #ffffff;
  }
  * { margin: 0; padding: 0; box-sizing: border-box; }
  html, body {
    width: 1200px;
    height: 1028px;
    overflow: hidden;
    background: var(--page);
    font-family: "Fira Sans", sans-serif;
  }
  .card {
    position: absolute;
    left: 310px;
    width: 579px;
    height: 330px;
    background: var(--card-dark);
    overflow: hidden;
  }
  .card--back { top: 165px; }
  .card--front { top: 532px; }
  .band-vertical {
    position: absolute;
    left: 67px;
    top: 0;
    width: 77px;
    height: 100%;
    background: var(--band-light);
  }
  .band-horizontal {
    position: absolute;
    left: 0;
    top: 127px;
    width: 100%;
    height: 76px;
    background: var(--band-light);
  }
  .holder-name {
    position: absolute;
    left: 144px;
    top: 137px;
    font-size: 43px;
    font-weight: 400;
    color: var(--ink-dark);
    letter-spacing: 0.5px;
    line-height: 1;
  }
  .contact {
    position: absolute;
    color: var(--ink-light);
    font-size: 21px;
    line-height: 28px;
    letter-spacing: 0.6px;
  }
  .card--back .contact { left: 172px; top: 224px; }
  .card--front .contact { left: 176px; top: 224px; }
  .brand-name {
    position: absolute;
    left: 70px;
    top: 145px;
    display: flex;
    align-items: center;
    gap: 12px;
    font-size: 34px;
    font-weight: 500;
    color: var(--ink-dark);
    letter-spacing: 6px;
    text-transform: uppercase;
    line-height: 1;
  }
  .brand-mark {
    width: 10px;
    height: 10px;
    border-radius: 50%;
    background: var(--ink-dark);
  }
</style>
</head>
<body>
  <section class="card card--back">
    <div class="band-vertical"></div>
    <div class="band-horizontal"></div>
    <p class="holder-name">Beatrice Morrow</p>
    <div class="contact">
      <p class="contact-phone">0455193786</p>
      <p class="contact-email">morrowinteriors@inbox.com</p>
    </div>
  </section>

  <section class="card card--front">
    <div class="band-vertical"></div>
    <div class="band-horizontal"></div>
    <div class="brand-name">
      <span class="brand-mark"></span>
      <span>Morrow Interiors</span>
    </div>
    <div class="contact">
      <p class="contact-phone">0455193786</p>
    </div>
  </section>
</body>
</html>
```